we need an experienced designer to design the tube for our toothpaste

Design guidelines:
1. On the front side, our product logo (‘K7320’) should be prominent enough.
2. Our brand logo (‘trelvine’) could be small-size and it's just a trademark indeed.

Some information here for your reference:
1. The color of toothpaste cap is white.
2. We hope that the primary color in the design is blue.
3.‘F’ in ‘K7320’ stands for ‘trelvine’ and ‘fluoride’.
4. We will use aluminum-plastic composite materials to make toothpaste tubes. In addition to the design, we also hope that you can make relevant suggestions on the special requirements of printing.

At last, we hope that you could submit both 2D design and 3D visual effects.

Colors
0094D4
00A9DD
6FCCEA
C7EBF8
E9F6FB

Requirements
Must have
• as attached

```html
<!DOCTYPE html>
<html lang="en">
<head>
<meta charset="utf-8">
<title>K7320 Orthodontic Toothpaste – Tube Artwork</title>
<link rel="stylesheet" href="https://fonts.googleapis.com/css2?family=Baloo+2:wght@800&family=Fira+Sans:wght@400;500;600;700;800&display=swap">
<style>
  :root {
    --blue: #4070aa;
    --blue-light: #7d9fcb;
    --blue-text: #4a74ad;
    --blue-soft: #6d8fbf;
    --white: #ffffff;
    --canvas: #f3f5f8;
    --gum: #e9b7ae;
  }
  * { box-sizing: border-box; margin: 0; padding: 0; }
  html, body { width: 1200px; height: 960px; overflow: hidden; }
  body {
    background: var(--canvas);
    font-family: "Fira Sans", sans-serif;
    position: relative;
  }
  .tube-panel {
    position: absolute;
    left: 80px;
    width: 1040px;
    height: 290px;
    background: var(--white);
    border-radius: 6px;
    overflow: hidden;
    box-shadow: 0 2px 10px rgba(40, 70, 120, 0.12);
  }
  .tube-panel--front { top: 140px; }
  .tube-panel--back { top: 530px; }
  .blue-field { position: absolute; inset: 0; }

  /* front */
  .product-mark {
    position: absolute;
    left: 50px; top: 18px;
    font-family: "Baloo 2", sans-serif;
    font-weight: 800;
    font-size: 128px;
    line-height: 1;
    color: var(--blue);
    letter-spacing: 2px;
  }
  .product-type {
    position: absolute; left: 54px; top: 160px;
    font-weight: 600; font-size: 17px; color: var(--blue-text);
  }
  .product-claims {
    position: absolute; left: 54px; top: 188px;
    font-size: 11.5px; line-height: 15px; color: var(--blue-soft);
    text-transform: uppercase;
  }
  .product-flavour {
    position: absolute; left: 54px; top: 230px;
    font-weight: 700; font-size: 20px; color: var(--blue-text);
  }
  .net-weight {
    position: absolute; left: 470px; top: 235px;
    font-size: 15px; color: var(--blue-soft);
  }
  .brand-name {
    position: absolute; right: 60px; top: 34px;
    font-weight: 800; font-size: 22px; color: var(--white);
  }
  .fluoride-claim {
    position: absolute; right: 60px; top: 120px;
    text-align: right; color: var(--white);
    font-weight: 700; font-size: 46px; line-height: 50px;
  }

  /* back */
  .copy-block {
    position: absolute; left: 54px; top: 50px; width: 580px;
    color: var(--blue-text);
  }
  .copy-block h3 { font-weight: 700; font-size: 12px; margin-bottom: 3px; }
  .copy-block p { font-size: 12px; line-height: 16px; margin-bottom: 12px; }
  .copy-block .muted { color: var(--blue-soft); }
  .care-heading {
    position: absolute; left: 920px; top: 28px; height: 240px;
    writing-mode: vertical-rl;
    color: var(--white); font-weight: 700; font-size: 20px; line-height: 24px;
    text-transform: uppercase;
  }
  .benefit-list {
    position: absolute; left: 770px; top: 30px; height: 240px;
    writing-mode: vertical-rl; list-style: none;
    display: flex; flex-wrap: wrap; gap: 0 4px; column-gap: 30px;
    color: var(--white); font-size: 12px; font-weight: 500; text-transform: uppercase;
  }
  .benefit-list li { margin-bottom: 18px; }
  .teeth-visual {
    position: absolute; left: 830px; width: 82px; height: 112px;
    background: linear-gradient(180deg, #f2d4cc, var(--gum));
  }
  .teeth-visual--plain { top: 24px; }
  .teeth-visual--braces { top: 150px; }
</style>
</head>
<body>

<section class="tube-panel tube-panel--front">
  <svg class="blue-field" viewBox="0 0 1040 290" preserveAspectRatio="none" aria-hidden="true">
    <defs>
      <linearGradient id="frontBlue" x1="0" y1="0" x2="0" y2="1">
        <stop offset="0" stop-color="#4070aa"/>
        <stop offset="1" stop-color="#7d9fcb"/>
      </linearGradient>
    </defs>
    <path d="M720 0 C650 60 730 120 670 170 C620 215 700 255 640 290 L1040 290 L1040 0 Z" fill="url(#frontBlue)"/>
    <circle cx="610" cy="160" r="48" fill="#7d9fcb"/>
    <circle cx="650" cy="75" r="26" fill="#4070aa"/>
    <circle cx="640" cy="30" r="14" fill="#4070aa"/>
  </svg>
  <div class="product-mark">K7320</div>
  <div class="product-type">ORTHODONTIC TOOTHPASTE</div>
  <div class="product-claims">Enhanced cavity prevention and gum protection<br>For use when wearing metal braces and clear aligners</div>
  <div class="product-flavour">DOUBLE MINT</div>
  <div class="net-weight">NET WT. 85g</div>
  <div class="brand-name">trelvine</div>
  <div class="fluoride-claim">Fluoride<br>1450 ppm</div>
</section>

<section class="tube-panel tube-panel--back">
  <svg class="blue-field" viewBox="0 0 1040 290" preserveAspectRatio="none" aria-hidden="true">
    <defs>
      <linearGradient id="backBlue" x1="0" y1="0" x2="0" y2="1">
        <stop offset="0" stop-color="#4070aa"/>
        <stop offset="1" stop-color="#7d9fcb"/>
      </linearGradient>
    </defs>
    <path d="M700 0 C640 60 720 130 660 180 C610 225 690 260 650 290 L1040 290 L1040 0 Z" fill="url(#backBlue)"/>
    <circle cx="620" cy="70" r="56" fill="#4070aa"/>
    <circle cx="650" cy="170" r="26" fill="#4070aa"/>
    <circle cx="615" cy="225" r="20" fill="#7d9fcb"/>
  </svg>
  <div class="copy-block">
    <h3>DIRECTIONS:</h3>
    <p>Apply at least one inch strip of the product onto a soft bristle toothbrush.<br>Brush teeth thoroughly, for at least three minutes twice a day.</p>
    <h3>INGREDIENTS:</h3>
    <p>Aqua, Sorbitol, Hydrated Silica, Glycerin, PEG-12, Sodium Lauryl Sulfate,<br>Aroma, Cellulose Gum, Titanium Dioxide, Potassium Sorbate, Allantoin,<br><span class="muted">Sodium Fluoride, Citric Acid, Peppermint Essence, Sodium Saccharin,<br>CI 47005, CI 42090, Cinnamal.</span></p>
    <h3>WARNINGS:</h3>
    <p class="muted">Do not ingest. Keep out of reach of children under 6 years of age.</p>
  </div>
  <ul class="benefit-list">
    <li>✓ Prevent cavity</li>
    <li>✓ Freshen breath</li>
    <li>✓ Strengthen teeth</li>
  </ul>
  <div class="teeth-visual teeth-visual--plain" role="img" aria-label="Illustration of healthy teeth and gums"></div>
  <div class="teeth-visual teeth-visual--braces" role="img" aria-label="Illustration of teeth with metal braces"></div>
  <div class="care-heading">Premium oral care during orthodontic treatment</div>
</section>

</body>
</html>
```